DOUBLE SIDED BROCHURE NEEDED TO PROMOTE DOCTOR

I need a double sided DL size (99mm x 210mm) brochure, promoting a doctor seeing patients in a new area.

I want something professional. I have included the relevant information. I would also like the Dr's picture somwhere in the brochure, with a professional background. I wish to print these tomorrow, so i will pick a winner within 14 hours of posting this ad.

I have included an example of a brochures design that I recently saw, and its definietly a good starting point.

Medical

```html
<!DOCTYPE html>
<html lang="en">
<head>
<meta charset="utf-8">
<title>Dr. Karim Haddad – Referral Brochure</title>
<link href="https://fonts.googleapis.com/css2?family=Exo+2:ital,wght@1,500;1,700;1,800&display=swap" rel="stylesheet">
<style>
  :root {
    --blue: #1aa7e4;
    --blue-deep: #0f93d6;
    --grey-light: #e4e6e8;
    --grey-mid: #c9ccd0;
    --charcoal: #45474a;
    --ink: #1b1b1d;
    --paper: #ffffff;
    --backdrop: #eef0f2;
  }
  * { margin: 0; padding: 0; box-sizing: border-box; }
  html, body {
    width: 1200px; height: 960px; overflow: hidden;
    background: var(--backdrop);
    font-family: "Exo 2", sans-serif;
    font-style: italic;
  }
  .sheet-pair {
    position: absolute; top: 70px; left: 184px;
    display: flex; gap: 60px;
  }
  .panel {
    position: relative; width: 386px; height: 820px;
    background: var(--paper); overflow: hidden;
    box-shadow: 0 6px 18px rgba(0,0,0,.15);
  }
  .panel-art { position: absolute; inset: 0; }

  /* front */
  .greeting {
    position: absolute; top: 62px; left: 22px;
    color: var(--paper); font-weight: 800; font-size: 23px;
  }
  .announcement {
    position: absolute; top: 412px; left: 24px; right: 24px;
    color: var(--blue-deep); font-size: 16px; font-weight: 500;
    line-height: 1.3; text-align: center;
  }
  .announcement strong { font-weight: 800; }
  .clinic-details {
    position: absolute; left: 22px; right: 22px; bottom: 26px;
    color: var(--paper); font-weight: 700; font-size: 14.5px; line-height: 1.35;
  }
  .clinic-row { display: flex; justify-content: space-between; align-items: flex-end; }
  .clinic-row .right { text-align: right; }
  .referral-note { margin-top: 16px; }

  /* back */
  .intro {
    position: absolute; top: 22px; left: 22px; right: 22px;
    color: var(--paper); font-weight: 700; font-size: 15px; line-height: 1.3;
  }
  .intro .name { color: var(--blue); }
  .specialty-list, .general-list {
    position: absolute; list-style: none;
    color: var(--ink); font-weight: 800;
  }
  .specialty-list { top: 232px; left: 24px; right: 20px; font-size: 18.5px; line-height: 1.3; }
  .general-heading {
    position: absolute; top: 528px; left: 24px;
    color: var(--blue); font-weight: 800; font-size: 18.5px;
    white-space: nowrap;
  }
  .general-list { top: 562px; left: 24px; font-size: 21px; line-height: 1.32; }
</style>
</head>
<body>
<main class="sheet-pair">

  <section class="panel panel-front">
    <svg class="panel-art" viewBox="0 0 386 820" width="386" height="820">
      <defs>
        <linearGradient id="portraitTone" x1="0" y1="0" x2="1" y2="1">
          <stop offset="0" stop-color="#9fb6c8"/>
          <stop offset="0.55" stop-color="#c7d6e2"/>
          <stop offset="1" stop-color="#3b3f47"/>
        </linearGradient>
      </defs>
      <path d="M0,0 H386 V96 Q200,46 0,34 Z" fill="var(--grey-light)"/>
      <path d="M0,34 Q200,46 386,96 V122 Q200,118 0,140 Z" fill="var(--blue)"/>
      <path d="M0,140 Q200,118 386,122 V132 Q200,130 0,152 Z" fill="var(--grey-mid)"/>
      <g role="img" aria-label="Portrait of the surgeon in front of a modern hospital building under a blue sky">
        <path d="M0,152 Q200,130 386,132 V392 Q150,384 0,320 Z" fill="url(#portraitTone)"/>
      </g>
      <path d="M0,300 Q150,370 386,380 V400 Q150,396 0,326 Z" fill="var(--blue)"/>
      <path d="M0,642 Q200,650 386,612 V624 Q200,662 0,656 Z" fill="var(--grey-mid)"/>
      <path d="M0,662 Q200,666 386,628 V820 H0 Z" fill="var(--blue-deep)"/>
    </svg>

    <h1 class="greeting">Dear Doctors,</h1>

    <p class="announcement">
      We are pleased to announce that <strong>Dr. Karim Haddad</strong> is now consulting in Seabrook, seeing public and private patients.
      <strong>Guaranteed</strong> appointment within two weeks, with patients having the option of surgery at Coastal Health Campus, Harbourside Hospital or St. Anne's Lakeside.
    </p>

    <footer class="clinic-details">
      <div class="clinic-row">
        <p>Seabrook Clinic:<br>42 Harbour View Road</p>
        <p class="right">Seabrook WA 6999.<br>Phone: 1300 555 012</p>
      </div>
      <p class="referral-note">Please send all referrals by fax to (08) 5550 1234.</p>
    </footer>
  </section>

  <section class="panel panel-back">
    <svg class="panel-art" viewBox="0 0 386 820" width="386" height="820">
      <defs>
        <linearGradient id="clinicTone" x1="0" y1="0" x2="1" y2="1">
          <stop offset="0" stop-color="#f2f3f4"/>
          <stop offset="0.5" stop-color="#d9dcdf"/>
          <stop offset="1" stop-color="#eceef0"/>
        </linearGradient>
      </defs>
      <path d="M0,0 H386 V196 Q200,150 0,84 Z" fill="var(--charcoal)"/>
      <path d="M0,84 Q200,150 386,196 V210 Q200,166 0,100 Z" fill="var(--blue)"/>
      <g role="img" aria-label="Soft-focus photo of a doctor's hands with a stethoscope">
        <path d="M0,100 Q200,166 386,210 V492 Q200,474 0,486 Z" fill="url(#clinicTone)"/>
      </g>
      <path d="M0,478 Q200,464 386,486 V500 Q200,482 0,496 Z" fill="var(--blue)"/>
      <path d="M0,496 Q200,482 386,500 V820 H0 Z" fill="#f1f2f3"/>
    </svg>

    <p class="intro"><span class="name">Dr. Haddad</span> is a highly trained specialised surgeon, in all areas of Endocrine, Breast and General Surgery. Including;</p>

    <ul class="specialty-list">
      <li>- Thyroid Surgery</li>
      <li>- Parathyroid surgery (including minimally</li>
      <li>- invasive parathyroidectomy)</li>
      <li>- Breast Cancer</li>
      <li>- Benign breast lesions</li>
    </ul>

    <h2 class="general-heading">All areas of general surgery, such as;</h2>
    <ul class="general-list">
      <li>- Gallbladder surgery</li>
      <li>- Hernia surgery</li>
      <li>- Haemorrhoids</li>
      <li>- Carpal Tunnel</li>
      <li>- Vasectomy etc etc...</li>
    </ul>
  </section>

</main>
</body>
</html>
```